Cosmetic Label Design for a Sunless Tanner

We need a label for a new sunless tanner. The label dye will be 2.5 inches in height by 6 inches in width. It will be laser printed by Brintova.net The label will be printed on gloss laminated white polypropylene self-adhesive material. A full project description can be found in the attached Word file. The label copy is also included in a Word file.

Target Market(s)

Females aged 18 to 35

Font styles to use
Serif

Colors

Designer to choose colors to be used in the design.

Requirements
Must have
• Clean look. Strong brand image.
Nice to have
• This is the first product in a future line. The design should have the ability to move to other products.
Should not have
• Too heavy. More than 4 colors. Fonts that are whimsical. Cursive writing. No cartoon like illustrations.

```html
<!DOCTYPE html>
<html lang="en">
<head>
<meta charset="utf-8">
<title>Nourishing Sunless Tanner Label</title>
<link rel="stylesheet" href="https://fonts.googleapis.com/css2?family=Oswald:wght@300;700&family=Roboto:wght@400&display=swap">
<style>
  :root {
    --backdrop: #8eadcd;
    --label-cream: #f2f1dc;
    --label-cream-light: #f8f7ea;
    --leaf-green: #b9cf6a;
    --leaf-pale: #e3e6bf;
    --title-green: #a3c83c;
    --title-shade: #7d9c2a;
    --brand-ink: #5d6b3a;
    --rule: #cfd1a4;
    --small-ink: #4d5234;
  }
  html, body {
    margin: 0;
    padding: 0;
    width: 1200px;
    height: 1200px;
    overflow: hidden;
    background: var(--backdrop);
  }
  .canvas {
    position: relative;
    width: 1200px;
    height: 1200px;
    display: flex;
    align-items: center;
    justify-content: center;
  }
  .label {
    position: relative;
    width: 1100px;
    height: 458px;
    background: radial-gradient(ellipse at 60% 45%, var(--label-cream-light) 0%, var(--label-cream) 70%);
    overflow: hidden;
  }
  .label-botanical {
    position: absolute;
    left: 0;
    top: 0;
    width: 300px;
    height: 100%;
    background: linear-gradient(160deg, var(--leaf-pale) 0%, rgba(185, 207, 106, 0.55) 55%, rgba(185, 207, 106, 0.15) 100%);
  }
  .label-content {
    position: absolute;
    left: 300px;
    right: 40px;
    top: 0;
    bottom: 0;
    display: flex;
    flex-direction: column;
    align-items: center;
  }
  .brand-name {
    margin-top: 62px;
    font-family: 'Oswald', sans-serif;
    font-weight: 300;
    font-size: 22px;
    letter-spacing: 1px;
    color: var(--brand-ink);
    text-transform: uppercase;
  }
  .brand-rule {
    width: 210px;
    height: 1px;
    margin-top: 16px;
    background: var(--rule);
  }
  .product-title {
    margin: 26px 0 0;
    font-family: 'Oswald', sans-serif;
    font-weight: 700;
    text-transform: uppercase;
    text-align: center;
    color: var(--title-green);
    text-shadow: 3px 3px 0 var(--title-shade);
    line-height: 0.98;
  }
  .product-title .line-1 { display: block; font-size: 62px; letter-spacing: 1px; }
  .product-title .line-2 { display: block; font-size: 94px; letter-spacing: 2px; }
  .product-title .line-3 { display: block; font-size: 94px; letter-spacing: 2px; }
  .net-volume {
    position: absolute;
    bottom: 24px;
    font-family: 'Roboto', sans-serif;
    font-size: 13px;
    color: var(--small-ink);
  }
</style>
</head>
<body>
  <main class="canvas">
    <section class="label">
      <div class="label-botanical" role="img" aria-label="Line illustration of bamboo stalks and palm fronds in soft green"></div>
      <div class="label-content">
        <p class="brand-name">Golden Habit</p>
        <div class="brand-rule"></div>
        <h1 class="product-title">
          <span class="line-1">Nourishing</span>
          <span class="line-2">Sunless</span>
          <span class="line-3">Tanner</span>
        </h1>
        <p class="net-volume">8 fl oz (237ml)</p>
      </div>
    </section>
  </main>
</body>
</html>
```